Inspiring book cover design (business book for designers and innovators)

I'm writing my first book, to be published early next year. I'm struggling to come up with an inspiring book cover design. I need your help!

Information to be included on the cover:
Book Title: Bright maker's manual
Subtitle: Designing products and services that make sense
Author: Marieke Vollen
Optional (not sure yet if I should include this on the cover): with online toolset

The book will be a square, size 170 x 170 mm
In the uploaded file you can find some example pages from the inside of the book. The cover design should fit with the design style of the example pages. The cover should "jump out" from the shelve in a bookstore and should attract designers, innovators, product managers, developers, and startup founders to buy the book.
Publisher: www.quarlomedia.example

About the book:
Why do some products fail while others become a success? Why do so many companies launch crappy products and services that nobody wants? This book is both a guide to and a source of inspiration for, designing products and services that make sense. Because if they make sense to people, people will want them.
In order for tech products and services to make sense, and create value for users, we need to apply technologies in a meaningful way. We can achieve this by designing strong benefits and at the same time minimizing resistance users might have against new technologies.
This book offers a complete overview of how to develop products and services that make sense: 27 ways to strengthen benefits and 28 ways to mitigate resistance. It offers practical insights, examples, tips, and tools to design products and services that people will love to use.

About the author:
https://www.profilehub.example/in/mariekevollen/

Target Market(s)

designers, innovators, product managers, developers, and startup founders

Industry/Entity Type

Design Agency

Font styles to use
Other font styles liked:
• You can choose. The inside of the book uses 3 fonts: LuloCleanW01-OneBold, Sansation, Segoe UI

Requirements
Must have
• Clean, yet creative design.
Square shape
Fits the design style of the example pages
Sans serif fonts. Do not have to be the same fonts like the ones that are used inside the book (LuloCleanW01-OneBold, Sansation, Segoe UI), but should go well with them.

Bright makers manual
48 ways to shape products and tools that feel right
Marieke Vollen
Nice to have
• I have several ideas that you might take as a starting point:
1) Do something with the left brain (rational, more digital) - right brain (creative, more emotional). For products to make sense, it needs to appeal to both parts of the brain
2) Work with a pattern, for example a (polygonal) triangular pattern
3) playful element in the letters, for example turning the O in innovator's into an on-off button or a stylish smiley, flipping the N in innovator's, doing something playful with the ' in innovator's
I've uploaded some images as a source of inspiration.

The cover should have a different color than the red/blue used in the example pages, but should fit the color palette that is used in the example pages.
Trigger curiosity.
Should not have
• Photographic pictures

```html
<!DOCTYPE html>
<html lang="en">
<head>
<meta charset="utf-8">
<title>Bright Makers Manual — Book Cover</title>
<link rel="stylesheet" href="https://fonts.googleapis.com/css2?family=Oswald:wght@400;500;600&display=swap">
<style>
  :root {
    --page-bg: #eceef2;
    --cover-navy: #1f2150;
    --cover-deep: #15173a;
    --cover-violet: #2c2b66;
    --glow-cyan: #2fb6e8;
    --glow-orange: #e5623a;
    --title-white: #f2f2f2;
    --accent-red: #cc344b;
    --band-blue: #2d6aad;
  }

  * { box-sizing: border-box; margin: 0; padding: 0; }

  html, body {
    width: 1200px;
    height: 840px;
    overflow: hidden;
    background: var(--page-bg);
  }

  .canvas {
    position: relative;
    width: 1200px;
    height: 840px;
    display: flex;
    align-items: center;
    justify-content: center;
  }

  .book-cover {
    position: relative;
    width: 740px;
    height: 740px;
    overflow: hidden;
    background: var(--cover-navy);
    box-shadow: 0 18px 40px rgba(20, 24, 60, 0.25);
    font-family: "Oswald", "Arial Narrow", sans-serif;
    text-transform: uppercase;
  }

  .cover-artwork {
    position: absolute;
    inset: 0;
    background:
      radial-gradient(ellipse 70% 8% at 55% 72%, rgba(47, 182, 232, 0.5), transparent 70%),
      radial-gradient(ellipse 45% 5% at 62% 66%, rgba(229, 98, 58, 0.4), transparent 70%),
      radial-gradient(ellipse 60% 30% at 70% 64%, rgba(47, 120, 200, 0.22), transparent 75%),
      linear-gradient(160deg, var(--cover-violet) 0%, var(--cover-navy) 45%, var(--cover-deep) 100%);
  }

  .cover-content {
    position: absolute;
    inset: 0;
    padding: 64px 56px;
  }

  .book-title {
    color: var(--title-white);
    font-weight: 600;
    font-size: 86px;
    line-height: 1;
    letter-spacing: 0.5px;
    white-space: nowrap;
    text-shadow: 3px 4px 6px rgba(0, 0, 0, 0.45);
  }

  .subtitle-row {
    display: flex;
    align-items: center;
    gap: 24px;
    margin-top: 52px;
  }

  .count-badge {
    flex: none;
    width: 120px;
    height: 120px;
    border-radius: 50%;
    background: var(--accent-red);
    display: flex;
    align-items: center;
    justify-content: center;
    color: var(--title-white);
    font-weight: 600;
    font-size: 66px;
    text-shadow: 2px 3px 4px rgba(0, 0, 0, 0.4);
  }

  .book-subtitle {
    color: var(--title-white);
    font-weight: 500;
    font-size: 32px;
    line-height: 1.12;
    letter-spacing: 0.3px;
    white-space: nowrap;
  }

  .book-author {
    margin-top: 44px;
    color: var(--accent-red);
    font-weight: 600;
    font-size: 80px;
    line-height: 1;
    letter-spacing: 1px;
    white-space: nowrap;
  }

  .toolset-band {
    position: absolute;
    right: 0;
    bottom: 48px;
    background: var(--band-blue);
    color: var(--title-white);
    font-weight: 400;
    font-size: 22px;
    letter-spacing: 0.5px;
    padding: 14px 34px 14px 30px;
    white-space: nowrap;
  }
</style>
</head>
<body>
  <main class="canvas">
    <article class="book-cover">
      <div class="cover-artwork" role="img" aria-label="Abstract glowing network of connected points with cyan and orange light streaks on a dark navy field"></div>
      <div class="cover-content">
        <h1 class="book-title">Bright makers<br>manual</h1>
        <div class="subtitle-row">
          <div class="count-badge">48</div>
          <p class="book-subtitle">Ways to shape products<br>and tools that feel right.</p>
        </div>
        <p class="book-author">Marieke Vollen</p>
      </div>
      <p class="toolset-band">With free online toolset</p>
    </article>
  </main>
</body>
</html>
```